Creative label for amber glass candle jar.

We are a candle company. Our products are handmade by us and natural. We are looking for something minimalistic and unique. We need a label for our candle jars (amber glass with black lid). Our current label doesn't match these requirements. We would like our products to be stocked in London shop, therefore design has to be up to a high standard. Jar specification Diameter (mm) 65 Height without cap (mm) 80. We want the new design to be different from the current one. It's just a guide for wording.
We should be able adjust the label, to change scent name.
Our scents are
*Coconut & Vanilla
*Lavender
*Bergamot
*Italian Garden
*Hygge
*Eucalyptus & Peppermint
*Coffee
*Cedarwood & Juniperberry
To know more about us, visit our website www.fenwickbrae.com or instagram.com/fenwickbrae
Good luck!
Industry/Entity Type
It Company
Colors
Designer to choose colors to be used in the design.
Requirements
Must have
- * I have attached two of our logos, label design must include one of them.
- *has to mention that it's made in London
- *has to say that candle is natural/made with essential oils
- *has to have scent name and No. on it..
- Label can be vertical or horizontal, but has to be square/rectangular,.
Should not have
- Label should not be round

```html
<!DOCTYPE html>
<html lang="en">
<head>
<meta charset="utf-8">
<title>brae candle labels</title>
<link href="https://fonts.googleapis.com/css2?family=Barlow+Semi+Condensed:wght@400;500;600;700&family=Exo+2:wght@400&display=swap" rel="stylesheet">
<style>
  :root {
    --backdrop: #323232;
    --paper: #ffffff;
    --ink: #1e1c1c;
    --edge-tone: #8e8d8d;
  }
  * { margin: 0; padding: 0; box-sizing: border-box; }
  html, body {
    width: 1200px; height: 640px; overflow: hidden;
    background: var(--backdrop);
  }
  .sheet { position: relative; width: 1200px; height: 640px; }

  .label {
    position: absolute;
    width: 27.5em; height: 27.6em;
    background: var(--paper);
    color: var(--ink);
    font-family: "Barlow Semi Condensed", "Arial Narrow", sans-serif;
    overflow: hidden;
    text-align: center;
  }
  .label--hero { font-size: 16px; left: 35px; top: 105px; }
  .label--mini { font-size: 7.2px; }
  .col-1 { left: 509px; } .col-2 { left: 738px; } .col-3 { left: 968px; }
  .row-1 { top: 103px; } .row-2 { top: 346px; }

  .brand-cap {
    position: absolute; left: 50%; top: 0;
    width: 11.875em; height: 5.94em;
    margin-left: -5.94em;
    background: var(--ink);
    border-radius: 0 0 5.94em 5.94em;
  }
  .brand-name {
    position: absolute; left: 0; right: 0; top: 0.78em;
    font-family: "Exo 2", sans-serif; font-weight: 400;
    font-size: 2em; line-height: 1; letter-spacing: 0.14em;
    color: var(--paper);
  }

  .edge-band {
    position: absolute; top: 3.1em; bottom: 0.875em; width: 1.6em;
    background: var(--edge-tone);
  }
  .edge-band--left { left: 0.2em; }
  .edge-band--right { right: 0.2em; }

  .scent-number, .scent-name, .scent-mood, .scent-note, .origin {
    position: absolute; left: 0; right: 0; line-height: 1; white-space: nowrap;
  }
  .scent-number { top: 8.15em; font-size: 1.4em; font-weight: 500; }
  .scent-number b { font-weight: 700; }
  .scent-name { top: 7.6em; font-size: 1.8em; font-weight: 700; letter-spacing: 0.08em; }
  .scent-name--long { letter-spacing: 0; font-size: 1.65em; top: 8.35em; }
  .scent-mood { top: 16.4em; font-size: 1em; font-weight: 500; letter-spacing: 0.32em; }
  .divider {
    position: absolute; left: 4.4em; right: 4.4em; top: 19.2em; height: 0.25em;
  }
  .divider svg { display: block; width: 100%; height: 100%; }
  .scent-note { top: 22.95em; font-size: 0.9em; font-weight: 400; }
  .origin { top: 32.8em; font-size: 0.7em; font-weight: 700; letter-spacing: 0.14em; }
  .flag { position: absolute; left: 50%; top: 24.75em; width: 2.5em; height: 1.6em; margin-left: -1.25em; }
  .flag svg { display: block; width: 100%; height: 100%; }
</style>
</head>
<body>
<svg width="0" height="0" style="position:absolute" aria-hidden="true">
  <defs>
    <symbol id="taper" viewBox="0 0 300 4" preserveAspectRatio="none">
      <polygon points="0,2 150,0 300,2 150,4" fill="#1e1c1c"/>
    </symbol>
    <symbol id="union-flag" viewBox="0 0 60 36">
      <rect width="60" height="36" fill="#1e1c1c"/>
      <path d="M0 0 L60 36 M60 0 L0 36" stroke="#fff" stroke-width="6"/>
      <path d="M0 0 L60 36 M60 0 L0 36" stroke="#1e1c1c" stroke-width="2"/>
      <path d="M30 0 V36 M0 18 H60" stroke="#fff" stroke-width="11"/>
      <path d="M30 0 V36 M0 18 H60" stroke="#1e1c1c" stroke-width="6"/>
    </symbol>
  </defs>
</svg>

<main class="sheet">
  <article class="label label--hero">
    <div class="brand-cap"><p class="brand-name">brae</p></div>
    <div class="edge-band edge-band--left" role="img" aria-label="Decorative striped border with chevrons"></div>
    <div class="edge-band edge-band--right" role="img" aria-label="Decorative striped border with chevrons"></div>
    <p class="scent-number"><b>№</b> 01</p>
    <h1 class="scent-name">LAVENDER</h1>
    <p class="scent-mood">COMFORT &amp; RELAXATION</p>
    <div class="divider"><svg><use href="#taper"/></svg></div>
    <p class="scent-note">Natural and made with essential oils</p>
    <p class="origin">MADE IN LONDON</p>
    <div class="flag"><svg><use href="#union-flag"/></svg></div>
  </article>

  <article class="label label--mini col-1 row-1">
    <div class="brand-cap"><p class="brand-name">brae</p></div>
    <div class="edge-band edge-band--left" role="img" aria-label="Decorative striped border with chevrons"></div>
    <div class="edge-band edge-band--right" role="img" aria-label="Decorative striped border with chevrons"></div>
    <p class="scent-number"><b>№</b>01</p>
    <h2 class="scent-name">LAVENDER</h2>
    <p class="scent-mood">COMFORT &amp; RELAXATION</p>
    <div class="divider"><svg><use href="#taper"/></svg></div>
    <p class="scent-note">Natural and made with essential oils</p>
    <p class="origin">MADE IN LONDON</p>
    <div class="flag"><svg><use href="#union-flag"/></svg></div>
  </article>

  <article class="label label--mini col-2 row-1">
    <div class="brand-cap"><p class="brand-name">brae</p></div>
    <div class="edge-band edge-band--left" role="img" aria-label="Decorative striped border with chevrons"></div>
    <div class="edge-band edge-band--right" role="img" aria-label="Decorative striped border with chevrons"></div>
    <p class="scent-number"><b>№</b>02</p>
    <h2 class="scent-name">BERGAMOT</h2>
    <p class="scent-mood">WITH AROMATIC ELEMENTS</p>
    <div class="divider"><svg><use href="#taper"/></svg></div>
    <p class="scent-note">Natural and made with essential oils</p>
    <p class="origin">MADE IN LONDON</p>
    <div class="flag"><svg><use href="#union-flag"/></svg></div>
  </article>

  <article class="label label--mini col-3 row-1">
    <div class="brand-cap"><p class="brand-name">brae</p></div>
    <div class="edge-band edge-band--left" role="img" aria-label="Decorative striped border with chevrons"></div>
    <div class="edge-band edge-band--right" role="img" aria-label="Decorative striped border with chevrons"></div>
    <p class="scent-number"><b>№</b>03</p>
    <h2 class="scent-name">ITALIAN GARDEN</h2>
    <p class="scent-mood">MEMORY BOOSTER</p>
    <div class="divider"><svg><use href="#taper"/></svg></div>
    <p class="scent-note">Natural and made with essential oils</p>
    <p class="origin">MADE IN LONDON</p>
    <div class="flag"><svg><use href="#union-flag"/></svg></div>
  </article>

  <article class="label label--mini col-1 row-2">
    <div class="brand-cap"><p class="brand-name">brae</p></div>
    <div class="edge-band edge-band--left" role="img" aria-label="Decorative striped border with chevrons"></div>
    <div class="edge-band edge-band--right" role="img" aria-label="Decorative striped border with chevrons"></div>
    <p class="scent-number"><b>№</b>05</p>
    <h2 class="scent-name scent-name--long">EUCALYPTUS &amp; PEPPERMINT</h2>
    <p class="scent-mood">REFRESHING &amp; MINTY</p>
    <div class="divider"><svg><use href="#taper"/></svg></div>
    <p class="scent-note">Natural and made with essential oils</p>
    <p class="origin">MADE IN LONDON</p>
    <div class="flag"><svg><use href="#union-flag"/></svg></div>
  </article>

  <article class="label label--mini col-2 row-2">
    <div class="brand-cap"><p class="brand-name">brae</p></div>
    <div class="edge-band edge-band--left" role="img" aria-label="Decorative striped border with chevrons"></div>
    <div class="edge-band edge-band--right" role="img" aria-label="Decorative striped border with chevrons"></div>
    <p class="scent-number"><b>№</b>06</p>
    <h2 class="scent-name">COFFEE</h2>
    <p class="scent-mood">ALLURING AROMA</p>
    <div class="divider"><svg><use href="#taper"/></svg></div>
    <p class="scent-note">Natural and made with essential oils</p>
    <p class="origin">MADE IN LONDON</p>
    <div class="flag"><svg><use href="#union-flag"/></svg></div>
  </article>

  <article class="label label--mini col-3 row-2">
    <div class="brand-cap"><p class="brand-name">brae</p></div>
    <div class="edge-band edge-band--left" role="img" aria-label="Decorative striped border with chevrons"></div>
    <div class="edge-band edge-band--right" role="img" aria-label="Decorative striped border with chevrons"></div>
    <p class="scent-number"><b>№</b>07</p>
    <h2 class="scent-name scent-name--long">CEDARWOOD &amp; JUNIPERBERRY</h2>
    <p class="scent-mood">RELAXING</p>
    <div class="divider"><svg><use href="#taper"/></svg></div>
    <p class="scent-note">Natural and made with essential oils</p>
    <p class="origin">MADE IN LONDON</p>
    <div class="flag"><svg><use href="#union-flag"/></svg></div>
  </article>
</main>
</body>
</html>
```